Cool wedding invitation

I need a creative graphic designer to create and design a hip, funky yet functional wedding invitation.

To give you an idea of what I am looking for I have create a Glimmerboard Board
http://www.glimmerboard-example.com/tanvelo/invitation/

Please provide your best 2 invitations.

Invitation #1 is designed to be printed on plastic. Use both sides
Invitation #2 is designed to be printed on cardboard

Don't be afraid to express your creativity.

Target Market(s)

This is a wedding invitation so the audience is primarily adults aged between 25 to 65.

Industry/Entity Type

Graphic Designer

Requirements
Nice to have
• The attached a colour palette outlines the colours the invitation may use.
• These colours will form the theme of the wedding.

```html
<!DOCTYPE html>
<html lang="en">
<head>
<meta charset="utf-8">
<title>Elaine &amp; Tom – Wedding Invitation</title>
<link rel="stylesheet" href="https://fonts.googleapis.com/css2?family=Lobster&family=Montserrat:wght@300;600&family=Ubuntu:ital,wght@1,400&display=swap">
<style>
  :root {
    --card: #ffffff;
    --lace: #7fcbc4;
    --lace-light: #bfe6e2;
    --lace-edge: #8fd2cc;
    --ink: #8a8a8a;
    --ornament: #ececec;
    --ornament-fade: #f8f8f8;
    --ampersand: #7ec8dd;
    --rule: #9fb8c4;
  }
  html, body {
    margin: 0;
    padding: 0;
    width: 1200px;
    height: 972px;
    overflow: hidden;
    background: var(--card);
  }
  .invitation {
    position: relative;
    width: 1200px;
    height: 972px;
    background: var(--card);
  }
  .lace-band {
    position: absolute;
    left: 0;
    top: 0;
    width: 360px;
    height: 972px;
  }
  .ornament {
    position: absolute;
    display: block;
  }
  .ornament--doves { left: 450px; top: 60px; width: 560px; height: 210px; }
  .ornament--flourish { left: 450px; top: 420px; width: 560px; height: 160px; }
  .couple {
    position: absolute;
    left: 450px;
    top: 290px;
    width: 560px;
    height: 120px;
    display: flex;
    align-items: baseline;
    justify-content: space-between;
    padding: 0 30px;
    box-sizing: border-box;
  }
  .couple__name {
    font-family: "Ubuntu", sans-serif;
    font-style: italic;
    font-size: 52px;
    color: var(--ink);
  }
  .couple__amp {
    font-family: "Lobster", cursive;
    font-size: 100px;
    line-height: 1;
    color: var(--ampersand);
  }
  .details {
    position: absolute;
    left: 455px;
    top: 628px;
    width: 680px;
    font-family: "Montserrat", sans-serif;
    color: var(--ink);
    text-transform: uppercase;
  }
  .details__line {
    margin: 0;
    font-size: 24px;
    line-height: 34px;
    letter-spacing: 2px;
    font-weight: 300;
    white-space: nowrap;
  }
  .details__line--time { letter-spacing: 7.2px; }
  .details__line strong { font-weight: 600; }
  .venue {
    position: absolute;
    left: 452px;
    top: 700px;
    margin: 0;
    font-family: "Lobster", cursive;
    font-weight: 400;
    font-size: 58px;
    color: var(--ink);
    white-space: nowrap;
  }
  .divider {
    position: absolute;
    left: 440px;
    top: 830px;
    width: 680px;
    height: 60px;
  }
</style>
</head>
<body>
<main class="invitation">
  <svg class="lace-band" viewBox="0 0 360 972" role="img" aria-label="Vertical band of white damask flowers and leaves on turquoise with a scalloped lace edge">
    <defs>
      <linearGradient id="laceFill" x1="0" y1="0" x2="1" y2="0">
        <stop offset="0" stop-color="var(--lace-light)"/>
        <stop offset="0.55" stop-color="var(--lace)"/>
        <stop offset="1" stop-color="var(--lace)"/>
      </linearGradient>
    </defs>
    <path d="M0 0 H300 Q345 54 300 108 Q345 162 300 216 Q345 270 300 324 Q345 378 300 432 Q345 486 300 540 Q345 594 300 648 Q345 702 300 756 Q345 810 300 864 Q345 918 300 972 H0 Z" fill="url(#laceFill)"/>
    <path d="M316 0 Q361 54 316 108 Q361 162 316 216 Q361 270 316 324 Q361 378 316 432 Q361 486 316 540 Q361 594 316 648 Q361 702 316 756 Q361 810 316 864 Q361 918 316 972" fill="none" stroke="var(--lace-edge)" stroke-width="3"/>
  </svg>

  <svg class="ornament ornament--doves" viewBox="0 0 560 210" role="img" aria-label="Two grey kissing doves above a symmetrical scrolled flourish">
    <defs>
      <radialGradient id="orn1" cx="0.5" cy="0.5" r="0.5">
        <stop offset="0" stop-color="var(--ornament)"/>
        <stop offset="1" stop-color="var(--ornament-fade)" stop-opacity="0"/>
      </radialGradient>
    </defs>
    <ellipse cx="280" cy="105" rx="280" ry="100" fill="url(#orn1)"/>
  </svg>

  <div class="couple">
    <span class="couple__name">Elaine</span>
    <span class="couple__amp">&amp;</span>
    <span class="couple__name">Tom</span>
  </div>

  <svg class="ornament ornament--flourish" viewBox="0 0 560 160" role="img" aria-label="Grey scrolled flourish with a small damask drop in the centre">
    <defs>
      <radialGradient id="orn2" cx="0.5" cy="0.5" r="0.5">
        <stop offset="0" stop-color="var(--ornament)"/>
        <stop offset="1" stop-color="var(--ornament-fade)" stop-opacity="0"/>
      </radialGradient>
    </defs>
    <ellipse cx="280" cy="80" rx="280" ry="75" fill="url(#orn2)"/>
  </svg>

  <section class="details">
    <p class="details__line"><strong>Twelve</strong> of <strong>July</strong> two thousand <strong>fourteen</strong></p>
    <p class="details__line details__line--time"><strong>Three</strong> o clock <strong>pm</strong> till <strong>late</strong></p>
  </section>

  <h1 class="venue">Harbourline Gallery, Sydney</h1>

  <svg class="divider" viewBox="0 0 680 60">
    <line x1="0" y1="30" x2="680" y2="26" stroke="var(--rule)" stroke-width="2"/>
    <ellipse cx="335" cy="28" rx="65" ry="16" fill="var(--ornament)" role="img" aria-label="Small looped knot ornament"/>
  </svg>
</main>
</body>
</html>
```